Roof Plumbing Company needs simple, modern business card using the attached logo and below details:

Dean Halloway
Summit Gutters Pty Ltd
ABN: 58 214 937 062
Phone: 0417 286 531
Email: summitgutters@mailbrook.com
Website: summitgutters.com.au

For all of your metal roof plumbing requirements contact Summit Gutters for an obligation free quote - no job too big or to small!

Industry/Entity Type

Business

Contact Information for Business Card

Dean Halloway
Summit Gutters Pty Ltd
ABN 58 214 937 062
0417 286 531
summitgutters@mailbrook.com
summitgutters.com.au

Requirements
Must have
• Bright eye catching design, professional look

```html
<!DOCTYPE html>
<html lang="en">
<head>
<meta charset="utf-8">
<title>Summit Gutters — Business Card</title>
<link rel="stylesheet" href="https://fonts.googleapis.com/css2?family=Montserrat:wght@400;500;700&display=swap">
<style>
  :root {
    --bg: #e6e3e0;
    --card: #ffffff;
    --brand-red: #9b1b1f;
    --corner-grey: #484848;
    --divider: #9a9a9a;
    --text: #3a3a3a;
  }
  * { margin: 0; padding: 0; box-sizing: border-box; }
  html, body {
    width: 1200px;
    height: 1000px;
    overflow: hidden;
    background: var(--bg);
  }
  .business-card {
    position: absolute;
    left: 100px;
    top: 205px;
    width: 1000px;
    height: 590px;
    background: var(--card);
    box-shadow: 0 10px 28px rgba(0, 0, 0, 0.22);
    font-family: "Montserrat", sans-serif;
    overflow: hidden;
  }
  .corner-accents {
    position: absolute;
    inset: 0;
    width: 100%;
    height: 100%;
  }
  .corner-accents .grey { fill: var(--corner-grey); }
  .corner-accents .red { fill: var(--brand-red); }

  .brand-name {
    position: absolute;
    left: 60px;
    top: 262px;
    width: 430px;
    display: flex;
    align-items: center;
    justify-content: center;
    gap: 14px;
    color: var(--brand-red);
    font-weight: 700;
    font-size: 38px;
    letter-spacing: 0.5px;
    text-transform: uppercase;
    white-space: nowrap;
  }
  .brand-mark {
    width: 22px;
    height: 22px;
    background: var(--brand-red);
    flex: none;
  }

  .divider {
    position: absolute;
    left: 521px;
    top: 137px;
    width: 3px;
    height: 307px;
    background: var(--divider);
  }

  .contact {
    position: absolute;
    left: 561px;
    top: 208px;
  }
  .contact-name {
    color: var(--brand-red);
    font-weight: 500;
    font-size: 35px;
    letter-spacing: 0.5px;
    text-transform: uppercase;
    line-height: 1.1;
    margin-bottom: 10px;
  }
  .contact-details {
    list-style: none;
    color: var(--text);
    font-weight: 400;
    font-size: 20.5px;
    line-height: 27px;
    padding-left: 4px;
  }
</style>
</head>
<body>
  <div class="business-card">
    <svg class="corner-accents" viewBox="0 0 694 407" preserveAspectRatio="none" aria-hidden="true">
      <polygon class="grey" points="632,0 694,0 694,135"/>
      <polygon class="red" points="608,0 632,0 694,135 694,162"/>
      <polygon class="grey" points="0,268 0,407 132,407"/>
      <polygon class="red" points="0,242 0,268 132,407 160,407"/>
    </svg>

    <div class="brand-name">
      <span class="brand-mark"></span>
      <span>Summit Gutters</span>
    </div>

    <div class="divider"></div>

    <div class="contact">
      <h1 class="contact-name">Dean Halloway</h1>
      <ul class="contact-details">
        <li>Summit Gutters Pty Ltd</li>
        <li>ABN 58 214 937 062</li>
        <li>0417 286 531</li>
        <li>summitgutters@mailbrook.com</li>
        <li>summitgutters.com.au</li>
      </ul>
    </div>
  </div>
</body>
</html>
```